Packing Design: SNACK FOOD BAG

We are manufactures and our main product is a kind of shell-shaped corn puff in ketchup flavor: brand name is Zebrin. (See photo Red Zebrin Flips Ketchup)

We will launch 15 new products (like chips, tortilla, popcorn, biscuits, etc.) under the same logo Zebrin.
As new Products are different, their layout must be different or with different designs.
But they must all be connected together with any feature, to be easily recognized / identified as same Zebrin range of products.
-

THE MAIN PURPOSE OF THIS PROJECT CONTEST IS:

Choosing the best connection between “Red Zebrin flips ketchup" label and new designs for new products.
Customers must easily understand that new products are done from same Zebrin Factory and are part of the same Zebrin brand (production). We want new labels to naturally derive from old Zebrin design with a modern and hip connection.

We would prefer drafts where 1 part is in red color (including Zebrin Logo) and the rest of layout to be used for different designs (for different products). At the end of all different designs, they may have in common a part of their layouts, derived from Red Zebrin Ketchup.
But we warmly welcome your different ideas and different suggestions.

-
Send sample draft for any from products below:
PEANUT BUTTER CORN bag size: High 210 mm x Width 145 mm
TORTILLA CHIPS ( flavors: Nachos / Spicy Ketchup) bag size: High 160 mm x Width 130 mm
CRUNCHY CROUTONS bag size: High 160 mm x Width 115 mm
CARAMEL CORN bag size: High 210 mm x Width 145 mm

Bags are (no transparent) BOPP material, with different sizes, containing small quantities from 20 – 50 grams.
-
Details for this project can be downloaded clicking to the link below:
http://www.filevault-example.net/file/4r8k21 and
http://www.filevault-example.net/file/w73m5q

Reason: there are designers submitting designs at the last moments. there is no time to review and give feedback to all. apologies for any inconvenience caused to the designers who submitted earlier warm regards

Target Market(s)

Target customers are young people: children, teens, students.

Industry/Entity Type

Factory

Requirements
Must have
• The new designs must include SAME Zebrin Logo, few pieces of the product view with flavor images and FEATURES CONNECTING ALL DESIGNS TOGETHER.
Nice to have
• A Feature is needed, to connect all new products with "Zebrin flips ketchup" design and all designs together.
Connections could be any details like:
RED COLORED ribbons, RED COLORED dotted /spotted layout,
RED COLORED background containing lines within itself,
different nuances of Zebrin Logo,
or else, or else, etc.
Show us what inspires you...

We would like to see strong deep colors, with 3D or fading reflections within them.
Final designs should bring the sense of appetite (making your mouth wet).
Should not have
• - Zebrin-Logo must be used without the word 'Flips"
- Must no have connection with ZEBRIN carton character.
- we don't like that all products to be in all-in-red bags.

```html
<!DOCTYPE html>
<html lang="en">
<head>
<meta charset="utf-8">
<title>Zebrin Snack Packaging</title>
<link rel="stylesheet" href="https://fonts.googleapis.com/css2?family=Signika:wght@600;700&family=Arimo&display=swap">
<style>
  :root {
    --canvas: #ffffff;
    --ink: #231f20;
    --label-ink: #333333;
    --tortilla-red: #ee4a24;
    --tortilla-light: #f6a592;
    --crouton-gold: #fbb91d;
    --crouton-light: #fde0a6;
    --chip-tone: #e9a632;
    --chili-tone: #e4284d;
    --cheese-tone: #f6e20e;
    --crouton-tone: #b9844c;
    --brand-green: #2e9a57;
    --mark-dot: #e8453c;
    --swatch-peanut: #bf6418;
    --swatch-nachos: #c5b900;
    --swatch-pizza: #008a3e;
    --swatch-caramel: #f6842a;
  }
  * { margin: 0; padding: 0; box-sizing: border-box; }
  html, body { width: 1200px; height: 1073px; overflow: hidden; background: var(--canvas); }
  .canvas { position: relative; width: 1200px; height: 1073px; }

  .bag {
    position: absolute; top: 95px; width: 455px; height: 657px;
    border: 2px solid var(--ink); overflow: hidden;
  }
  .bag--tortilla { left: 103px; background: linear-gradient(125deg, var(--tortilla-red) 30%, #f17556 58%, var(--tortilla-light) 78%); }
  .bag--croutons { left: 650px; background: linear-gradient(125deg, var(--crouton-gold) 32%, #fcc757 58%, var(--crouton-light) 80%); }
  .bag__corner { position: absolute; inset: 0; width: 100%; height: 100%; }

  .maker-mark {
    position: absolute; left: 24px; top: 40px;
    display: flex; align-items: center; gap: 5px;
    font-family: "Signika", sans-serif; font-weight: 700; font-size: 17px;
    color: var(--brand-green);
  }
  .maker-mark__dot { width: 14px; height: 14px; border-radius: 50%; background: var(--mark-dot); }

  .brand-name {
    position: absolute; left: 30px; top: 95px; width: 400px; text-align: center;
    font-family: "Signika", sans-serif; font-weight: 700; font-size: 124px; line-height: 1;
    color: var(--ink);
  }

  .product-title {
    position: absolute; font-family: "Signika", sans-serif; font-weight: 700;
    color: var(--ink); white-space: nowrap; line-height: 1;
  }
  .product-flavour {
    position: absolute; font-family: "Signika", sans-serif; font-weight: 600;
    color: var(--ink); line-height: 1.05;
  }
  .bag--tortilla .product-title { left: 56px; top: 308px; font-size: 42px; letter-spacing: 1.6px; }
  .bag--tortilla .product-flavour { left: 63px; top: 355px; font-size: 33px; }
  .bag--croutons .product-title { left: 57px; top: 307px; font-size: 38px; letter-spacing: 0; }
  .bag--croutons .product-flavour { left: 60px; top: 356px; font-size: 33px; }
  .product-flavour span { display: block; }
  .product-flavour .indent { padding-left: 7px; }

  .art { position: absolute; border-radius: 10px; }
  .art--chips { left: 237px; top: 440px; width: 216px; height: 215px; background: linear-gradient(160deg, #f3c25a, var(--chip-tone)); }
  .art--chili { left: 65px; top: 527px; width: 117px; height: 88px; background: linear-gradient(135deg, #ec5a6f, var(--chili-tone)); }
  .art--cheese { left: 68px; top: 530px; width: 122px; height: 85px; background: var(--cheese-tone); }
  .art--croutons { left: 245px; top: 460px; width: 195px; height: 180px; background: linear-gradient(150deg, #d9ad72, var(--crouton-tone)); }

  .swatch { position: absolute; top: 841px; width: 164px; height: 110px; }
  .swatch--peanut { left: 105px; background: var(--swatch-peanut); }
  .swatch--nachos { left: 364px; background: var(--swatch-nachos); }
  .swatch--pizza { left: 664px; background: var(--swatch-pizza); }
  .swatch--caramel { left: 938px; background: var(--swatch-caramel); }
  .swatch-label {
    position: absolute; top: 967px; font-family: "Arimo", sans-serif; font-size: 18.5px;
    color: var(--label-ink); white-space: nowrap; transform: translateX(-50%);
  }
</style>
</head>
<body>
<main class="canvas">
  <section class="bag bag--tortilla">
    <svg class="bag__corner" viewBox="0 0 455 657" preserveAspectRatio="none" aria-hidden="true">
      <polygon points="455,352 455,657 234,657" fill="#ffffff"/>
    </svg>
    <div class="maker-mark"><span class="maker-mark__dot"></span>Sunnel</div>
    <div class="brand-name">Zebrin</div>
    <h2 class="product-title">TORTILLA CHIPS</h2>
    <p class="product-flavour">Spicy Ketchup</p>
    <div class="art art--chili" role="img" aria-label="Red chili pepper illustration"></div>
    <div class="art art--chips" role="img" aria-label="Photo of tortilla chips"></div>
  </section>

  <section class="bag bag--croutons">
    <svg class="bag__corner" viewBox="0 0 455 657" preserveAspectRatio="none" aria-hidden="true">
      <defs>
        <linearGradient id="crouton-fade" x1="0" y1="0" x2="1" y2="1">
          <stop offset="0" stop-color="#ffffff" stop-opacity="0.4"/>
          <stop offset="0.5" stop-color="#ffffff"/>
        </linearGradient>
      </defs>
      <polygon points="455,372 455,657 250,657" fill="url(#crouton-fade)"/>
    </svg>
    <div class="maker-mark"><span class="maker-mark__dot"></span>Sunnel</div>
    <div class="brand-name">Zebrin</div>
    <h2 class="product-title">CRUNCHY CROUTONS</h2>
    <p class="product-flavour"><span>Cheese &amp; Spicy</span><span class="indent">Ketchupherbs</span></p>
    <div class="art art--cheese" role="img" aria-label="Cheese wedge illustration"></div>
    <div class="art art--croutons" role="img" aria-label="Photo of toasted croutons"></div>
  </section>

  <div class="swatch swatch--peanut"></div>
  <div class="swatch swatch--nachos"></div>
  <div class="swatch swatch--pizza"></div>
  <div class="swatch swatch--caramel"></div>
  <p class="swatch-label" style="left:191px">PEANUT BUTTER CORN</p>
  <p class="swatch-label" style="left:449px">TORTILLA CHIPS/Nachos</p>
  <p class="swatch-label" style="left:756px">CRUNCHY CROUTONS/ Italian Pizza</p>
  <p class="swatch-label" style="left:1021px">CARAMEL CORN</p>
</main>
</body>
</html>
```